Media/PR business needs a website upgrade

Modernise my website www.vrl.net.au into a simpler and mobile friendly site with the usual plugins, maximum 5 pages, 4 might be enough. My page is already hosted and I have an email address so I just want to work with a designer who is fantastic with WordPress, to refresh and simplify the 6 year-old look.

Target Market(s)

men & women 25-55

Industry/Entity Type

Business

Coding

Coded - Design and coding required

Number of Pages Required

4 page

Font styles to use
Sans Serif

Colors
f37122
ffffff

Requirements
Must have
• Social media plugins, about, client portfolio, contact (can be under about)blog capability
Nice to have
• photos of jobs I've done
Should not have
• e-commerce, can lose all the client logos

```html
<!DOCTYPE html>
<html lang="en">
<head>
<meta charset="utf-8">
<title>Vela Ridge Liaison</title>
<link href="https://fonts.googleapis.com/css2?family=Arimo:wght@400;700&display=swap" rel="stylesheet">
<style>
:root{
  --orange:#f37122;
  --white:#ffffff;
  --page-grey:#c9c9c9;
  --dark:#323232;
  --card:#1d1d1d;
  --ink:#3a3a3a;
  --muted:#6b6b6b;
  --light-text:#a9a9a9;
  --heading-light:#e6e6e6;
  --numeral:#8d8d8d;
}
*{box-sizing:border-box;margin:0;padding:0}
html,body{width:1200px;height:1200px;overflow:hidden;background:var(--white);font-family:"Arimo",Arial,sans-serif}
.site{position:absolute;left:370px;top:14px;width:514px;height:1310px;transform:scale(.895);transform-origin:0 0;background:var(--page-grey)}
.abs{position:absolute}
/* hero */
.hero{left:0;top:0;width:514px;height:200px;background:linear-gradient(180deg,#55647a 0%,#6f7f92 22%,#2d3f58 48%,#1d2f45 72%,#2a2f36 100%)}
.brand{left:20px;top:10px;display:flex;align-items:center;gap:5px;color:var(--white);font-size:7px;line-height:7px;font-weight:700;width:110px}
.brand-dot{width:30px;height:30px;border-radius:50%;background:var(--orange);flex:none}
.phone-btn{left:410px;top:0;width:84px;height:20px;background:var(--orange);color:var(--white);font-size:7px;display:flex;align-items:center;gap:4px;padding-left:10px}
.nav{right:20px;top:30px;display:flex;gap:6px;font-size:6px;color:var(--white);text-transform:uppercase}
.nav span::before{content:"";display:inline-block;width:3px;height:3px;border:1px solid var(--orange);border-radius:50%;margin-right:4px;vertical-align:middle}
.nav .on{color:var(--orange)}
.arrow{width:12px;height:12px;border-radius:50%;background:rgba(255,255,255,.85)}
.dots{left:245px;top:178px;display:flex;gap:3px}
.dots i{width:4px;height:4px;border-radius:50%;background:var(--white)}
.dots i:first-child{background:var(--orange)}
/* panels */
.panel{background:var(--white)}
.numeral{font-size:30px;font-weight:700;color:var(--numeral);letter-spacing:-2px;line-height:30px}
.rule{width:2px;background:var(--orange)}
.title{font-size:10px;color:var(--ink);text-transform:uppercase}
.title.on-dark{color:var(--heading-light)}
.copy{font-size:5.6px;line-height:7px;color:var(--muted);text-align:justify}
.copy p{margin-bottom:4px}
.lead{font-size:11px;line-height:10.5px;color:var(--ink);letter-spacing:-.3px}
.lead b{color:var(--orange)}
.photo{border:0}
/* services */
.services{left:0;top:412px;width:514px;height:643px;background:var(--dark)}
.card{position:absolute;width:138px;height:185px;background:var(--card)}
.card .photo{position:absolute;left:0;top:0;width:138px;height:75px}
.card h4{position:absolute;left:5px;top:85px;font-size:5.8px;color:var(--orange);text-transform:uppercase}
.card .copy{position:absolute;left:5px;top:94px;width:122px;height:80px;overflow:hidden;color:var(--light-text)}
.card .bar{position:absolute;right:4px;top:94px;width:3px;height:80px;background:#4a4a4a}
.fbbox{left:361px;top:0;width:153px;height:236px;background:var(--white)}
.fbhead{left:0;top:0;width:153px;height:76px;background:linear-gradient(160deg,#8a8a8a,#2b2b2b)}
.fbname{font-size:9px;font-weight:700;color:var(--white)}
.btn-small{font-size:5px;background:var(--white);color:var(--ink);padding:2px 4px;border-radius:1px}
.thumbs{display:flex;gap:2px}
.thumbs i{width:15px;height:15px;background:linear-gradient(135deg,#6d7f95,#3f4c5b)}
/* contact */
.field{position:absolute;left:252px;width:192px;height:11px;border:1px solid #c3c3c3;background:var(--white)}
.flabel{position:absolute;left:252px;font-size:5.5px;color:var(--muted)}
.info b{display:block;font-size:6px;color:var(--ink)}
.info span{display:block;font-size:5.6px;color:var(--muted);margin-bottom:5px}
.social{display:flex;gap:6px}
.social i{width:31px;height:31px;border-radius:50%}
.foot{font-size:5.5px;color:var(--muted)}
.foot span::before{content:"";display:inline-block;width:3px;height:3px;border:1px solid var(--orange);border-radius:50%;margin:0 4px 0 6px;vertical-align:middle}
</style>
</head>
<body>
<div class="site">

  <!-- hero -->
  <div class="abs hero" role="img" aria-label="Photo of a regatta fleet with colourful spinnakers beside a waterfront yacht club"></div>
  <div class="abs brand"><span class="brand-dot"></span><span>Vela Ridge Liaison</span></div>
  <div class="abs phone-btn">
    <svg width="9" height="9" viewBox="0 0 10 10"><rect x="0" y="0" width="10" height="10" rx="1" fill="#fff"/><path d="M3 2.2l1 1.6-.6.8c.5 1 1.1 1.6 2 2l.8-.6 1.6 1-.5 1.2c-2.6-.3-4.5-2.3-4.9-4.8z" fill="#f37122"/></svg>
    +61 400 555 012
  </div>
  <div class="abs nav"><span class="on">Home</span><span>Projects / Event</span><span>Client</span><span>Testimonials</span><span>Blog</span></div>
  <div class="abs arrow" style="left:9px;top:100px"></div>
  <div class="abs arrow" style="left:491px;top:100px"></div>
  <div class="abs dots"><i></i><i></i><i></i><i></i></div>

  <!-- intro + about -->
  <div class="abs panel" style="left:10px;top:210px;width:493px;height:192px"></div>
  <div class="abs numeral" style="left:18px;top:222px">01</div>
  <div class="abs rule" style="left:55px;top:225px;height:162px"></div>
  <div class="abs lead" style="left:65px;top:225px;width:188px">VELA RIDGE LIAISON IS AN <b>ESTABLISHED SPECIALIST PUBLIC RELATIONS</b> AND <b>EVENT MANAGEMENT BUSINESS.</b></div>
  <div class="abs photo" role="img" aria-label="Portrait of the founder" style="left:65px;top:271px;width:77px;height:116px;background:linear-gradient(180deg,#b7b9b3,#3b6fa5)"></div>
  <div class="abs copy" style="left:146px;top:271px;width:103px">
    <p>With a communications degree and 20 plus years experience working in public relations, publicity, media and project management, VRL founder Dana Whitmore offers a complete contract based option for your next major sporting, social, cultural or community event.</p>
    <p>Contact Dana at VRL for strategic advice on sponsorship spend and how to leverage your investment, and to tap into her extensive media and professional network.</p>
    <p>Flexible, composed and relationship focused freelancer ready to start work.</p>
  </div>

  <div class="abs numeral" style="left:258px;top:222px">02</div>
  <div class="abs rule" style="left:297px;top:225px;height:162px"></div>
  <div class="abs title" style="left:306px;top:237px">About</div>
  <div class="abs copy" style="left:306px;top:258px;width:188px">
    <p>Dana grew up on Heron Island in Bayside on the northern beaches, the breeding ground for many Australian sailing greats including some of the best known racing families.</p>
    <p>As a 'tinny terror' she attended the local public school then Bayside High School with some of these sailing families, and now through her work she's back mingling with the greats.</p>
    <p>A communications degree at university, a career that has seen her rise to the top of her specialist field and three children later has brought her full circle back to the island as a home owner.</p>
    <p>Sailing-wise the women's twilight at the Northshore Yacht Club, regular family campaign at the national championship and more recently a campaign for the world titles, plus the odd guest spot at regattas, keeps her in touch and active, as does regular Pilates.</p>
    <p>Being a thoughtful mother &amp; partner, running a successful business and being a good friend maintain Dana's busy and well-rounded life.</p>
  </div>

  <!-- services -->
  <div class="abs services">
    <div class="abs numeral" style="left:18px;top:15px">03</div>
    <div class="abs rule" style="left:55px;top:18px;height:610px"></div>
    <div class="abs title on-dark" style="left:64px;top:28px">Services</div>

    <div class="card" style="left:65px;top:51px">
      <div class="photo" role="img" aria-label="Photo of surf lifesaving boards on a beach" style="background:linear-gradient(180deg,#9fb6c7,#d8c9b1)"></div>
      <h4>Sports Media</h4>
      <div class="copy"><p>VRL founder Dana Whitmore has worked closely with Australian and international sports media since 1996.</p><p>Dana has a thorough understanding of the media's requirements for a strong story angle, good talent, photography and deadlines, and finding the harmony between delivering to media and satisfying the client's brief. Key events include the annual sailing world cup and festival of sails.</p></div>
      <div class="bar"></div>
    </div>
    <div class="card" style="left:213px;top:51px">
      <div class="photo" role="img" aria-label="Photo of yachts racing past a clubhouse" style="background:linear-gradient(180deg,#6f8fb0,#4a5661)"></div>
      <h4>Publicity</h4>
      <div class="copy"><p>Generating media publicity for both the event and its sponsor is one of Dana's key strengths and drivers.</p><p>She works with clients to establish objectives and target audiences then develops a PR/media plan to deliver on the brief. From long lead magazines and social media campaigns through to short lead opportunities, media attendance at the event and the resulting coverage, VRL will stay calm and focused.</p></div>
      <div class="bar"></div>
    </div>

    <div class="abs fbbox">
      <div class="abs fbhead" role="img" aria-label="Cover photo of a sailing event"></div>
      <div class="abs" style="left:8px;top:10px;width:26px;height:26px;background:#c9a88a;border:2px solid #fff"></div>
      <div class="abs fbname" style="left:40px;top:10px">VRL - Dana Whitmore</div>
      <div class="abs" style="left:40px;top:21px;font-size:6px;color:#fff">410 likes</div>
      <div class="abs btn-small" style="left:8px;top:55px">Like Page</div>
      <div class="abs btn-small" style="left:112px;top:53px">Share</div>
      <div class="abs" style="left:6px;top:89px;font-size:5px;color:var(--muted)">Be the first of your friends to like this</div>
      <div class="abs thumbs" style="left:6px;top:98px"><i></i><i></i><i></i><i></i><i></i><i></i><i></i></div>
      <div class="abs" style="left:6px;top:124px;width:24px;height:24px;background:#c9a88a"></div>
      <div class="abs" style="left:36px;top:128px;font-size:7px;color:var(--ink)">VRL - Dana Whitmore</div>
      <div class="abs" style="left:36px;top:137px;font-size:5px;color:var(--muted)">7 hours ago</div>
      <div class="abs" style="left:136px;top:128px;width:8px;height:8px;background:#4267b2"></div>
      <div class="abs copy" style="left:6px;top:152px;width:140px;font-size:5px;line-height:6px">A great initiative by Global Sailing League, looking forward to listening in to the panel members and I encourage all Australian yacht clubs to join the conversation. Harbour clubs, bay clubs, river clubs and ocean clubs from every state are welcome to take part and share ideas on growing our sport together. #UnitingOurSport</div>
    </div>

    <div class="card" style="left:65px;top:246px">
      <div class="photo" role="img" aria-label="Photo of a sponsored racing catamaran crew" style="background:linear-gradient(180deg,#8797a8,#27313b)"></div>
      <h4>Sponsorship Leverage</h4>
      <div class="copy"><p>Dana has worked with many sponsors including premium brand clients Meridian Watches, Coastline Motors and Harbour Auto Group.</p><p>Regardless of stature or spend, Dana will advise honestly on what the client can expect in terms of mainstream and specialist media coverage, but also look for other opportunities to reach target audiences via social media, local media, signage and cooperative partnerships.</p></div>
      <div class="bar"></div>
    </div>
    <div class="card" style="left:213px;top:246px">
      <div class="photo" role="img" aria-label="Photo of a crowd at a prize giving" style="background:linear-gradient(180deg,#b5434a,#e3e3e3)"></div>
      <h4>Event Management</h4>
      <div class="copy"><p>From planning through to execution and follow up, VRL provides a complete service.</p><p>Skilled in broader event planning including signage, entertainment and photography through to the media component including media accreditation, press packs, designing a working media centre and being hands-on at the event.</p><p>VRL has a number of specialised subcontractors to call on if the event is significant in size.</p></div>
      <div class="bar"></div>
    </div>
    <div class="card" style="left:361px;top:246px">
      <div class="photo" role="img" aria-label="Photo of spectators waving flags" style="background:linear-gradient(180deg,#c8c8c8,#a34b4b)"></div>
      <h4>Crisis Management</h4>
      <div class="copy"><p>Every event should have an emergency management plan.</p><p>Businesses, community organisations and sponsors who understand well ahead how they are going to communicate with their stakeholders, as well as the media, during a crisis will handle the situation far better.</p></div>
    </div>

    <div class="card" style="left:65px;top:441px">
      <div class="photo" role="img" aria-label="Photo of sailors at a press conference" style="background:linear-gradient(180deg,#7b6a5e,#2d3545)"></div>
      <h4>Social Media</h4>
      <div class="copy"><p>Dana can create the client's presence and supply or edit content for whichever medium the client nominates.</p></div>
    </div>
    <div class="card" style="left:213px;top:441px">
      <div class="photo" role="img" aria-label="Photo of skippers with a trophy" style="background:linear-gradient(180deg,#a28c73,#3a3a3a)"></div>
      <h4>Event Management</h4>
      <div class="copy"><p>From planning through to execution and follow up, VRL provides a complete service.</p><p>Skilled in broader event planning including signage, entertainment and photography through to the media component including media accreditation, press packs, designing a working media centre and being hands-on at the event.</p><p>VRL has a number of specialised subcontractors to call on if the event is significant in size.</p></div>
      <div class="bar"></div>
    </div>
    <div class="card" style="left:361px;top:441px">
      <div class="photo" role="img" aria-label="Photo of a marina with flags and masts" style="background:linear-gradient(180deg,#6c8a5a,#4d6f9a)"></div>
      <h4>Crisis Management</h4>
      <div class="copy"><p>Every event should have an emergency management plan.</p><p>Businesses, community organisations and sponsors who understand well ahead how they are going to communicate with their stakeholders, as well as the media, during a crisis will handle the situation far better.</p></div>
    </div>
  </div>

  <!-- contact -->
  <div class="abs panel" style="left:10px;top:1063px;width:493px;height:212px"></div>
  <div class="abs numeral" style="left:18px;top:1080px">04</div>
  <div class="abs rule" style="left:55px;top:1083px;height:177px"></div>
  <div class="abs title" style="left:64px;top:1092px">Contact</div>
  <div class="abs info" style="left:64px;top:1115px;width:170px">
    <b>PHONE :</b><span>+61 400 555 012</span>
    <b>ADDRESS :</b><span>PO Box 220, Harbourside NSW 2000 Australia</span>
    <b>EMAIL :</b><span>dana@vrl.net.au</span>
    <b>ABN :</b><span>12 345 678 901</span>
  </div>
  <div class="abs" style="left:64px;top:1196px;width:172px;border-top:1px dotted #9a9a9a"></div>
  <div class="abs lead" style="left:64px;top:1205px;font-size:8px;line-height:8.5px">PLEASE <b>CHECK IN OUR SOSIAL MEDIA</b><br>AND <b>SHARING</b> TO ALL</div>
  <div class="abs social" style="left:64px;top:1230px">
    <i role="img" aria-label="Social link one" style="background:#3b5a9a"></i>
    <i role="img" aria-label="Social link two" style="background:#29b5e3"></i>
    <i role="img" aria-label="Social link three" style="background:#3a8fd0"></i>
  </div>

  <div class="flabel" style="top:1115px">Name :</div><div class="field" style="top:1125px"></div>
  <div class="flabel" style="top:1142px">Email :</div><div class="field" style="top:1152px"></div>
  <div class="flabel" style="top:1169px">Subject :</div><div class="field" style="top:1179px"></div>
  <div class="flabel" style="top:1196px">Messege :</div><div class="field" style="top:1206px;height:54px"></div>
  <div class="abs" style="left:449px;top:1248px;width:45px;height:12px;background:#2f2f2f;color:#bbb;font-size:5.5px;text-align:center;line-height:12px">SEND</div>

  <!-- footer -->
  <div class="abs foot" style="left:4px;top:1289px"><span>Home</span><span>Projects / Event</span><span>Client</span><span>Testimonials</span><span>Blog</span></div>
  <div class="abs foot" style="right:11px;top:1289px">Copyright © 2017 Vela Ridge Liaison &nbsp;|&nbsp; All rights reserved</div>
</div>
</body>
</html>
```